Lumen Ridge Heart Marketing Folder

We are a cardiology clinic. Our primary colors are black and red. We are looking for a design that can be used for a 9 by 12 folder with two inner pockets. It will be used to provide patients with educational materials for all the services we provide. We have a specialized PET CT on site. I am uploading a list of ALL our services. I am also uploading our office logo to be used. We would like the services, logo, office address, phone, fax, email, and website used. Our Phone is 555-318-2764, Fax is 555-318-2765, address is 712 Fenwick Ln. Ste. D, Webster, TX 70000, website is www.lumenridgeheart.example, email is info@lumenridgeheart.example. We have four physicians: For the uploaded photo they are in this order: Marisol Okafor, MD, Valentino Greaves, MD, Dmitri Lundqvist, MD, and Corwin Lundqvist, MD. I am also uploading their group photo that can be used as well.

Target Market(s)

Our Patients

Industry/Entity Type

Health Care

Font styles to use
Serif

Colors
ec1f27

Requirements
Must have
• Preferred Colors are black and red.
Logo
Name: Lumen Ridge Heart
Address, Phone, Fax, website, email
Services Provided
Nice to have
• Open to suggestions

```html
<!DOCTYPE html>
<html lang="en">
<head>
<meta charset="utf-8">
<title>Lumen Ridge Heart – Folder Inside Spread</title>
<link rel="stylesheet" href="https://fonts.googleapis.com/css2?family=Nunito+Sans:wght@400;600;800&display=swap">
<style>
  :root {
    --page-bg: #ffffff;
    --panel-dark: #1d1819;
    --pattern-tone: #3a2a2a;
    --pattern-red: #7a1f25;
    --band-red: #d4232c;
    --pocket-red: #c1343e;
    --pocket-deep: #9a2c37;
    --fold-line: #b3252d;
    --text-light: #f3eeee;
    --heart-tone: rgba(120, 28, 34, 0.28);
  }
  * { margin: 0; padding: 0; box-sizing: border-box; }
  html, body {
    width: 1200px; height: 800px; overflow: hidden;
    background: var(--page-bg);
    font-family: "Nunito Sans", Arial, sans-serif;
  }
  .folder-spread {
    position: absolute; left: 40px; top: 5px;
    width: 1120px; height: 790px;
    background: var(--panel-dark);
    overflow: hidden;
  }
  .hex-pattern {
    position: absolute; left: 0; top: 0; width: 100%; height: 230px;
    background:
      radial-gradient(ellipse 260px 140px at 96% 20%, rgba(150, 35, 40, 0.55), transparent 70%),
      radial-gradient(ellipse 300px 120px at 55% 25%, rgba(90, 78, 70, 0.45), transparent 70%),
      radial-gradient(ellipse 240px 110px at 8% 10%, rgba(110, 40, 40, 0.5), transparent 70%),
      linear-gradient(180deg, var(--pattern-tone) 0%, rgba(29, 24, 25, 0) 100%);
  }
  .heart-mark {
    position: absolute; left: 361px; top: 164px; width: 401px; height: 363px;
    background: radial-gradient(ellipse at 50% 45%, var(--heart-tone), transparent 70%);
  }
  .fold-line {
    position: absolute; left: 560px; top: 0; height: 100%;
    border-left: 1px dashed var(--fold-line);
    opacity: 0.8;
  }
  .section-band {
    position: absolute; left: 0; top: 49px; width: 620px; height: 35px;
    background: linear-gradient(90deg, var(--band-red) 0%, var(--band-red) 45%, rgba(212, 35, 44, 0) 100%);
  }
  .section-title {
    position: absolute; left: 51px; top: 50px;
    font-weight: 800; font-size: 19px; line-height: 33px;
    color: #ffffff;
  }
  .service-list {
    position: absolute; list-style: none;
    font-size: 12.6px; line-height: 18px; color: var(--text-light);
  }
  .service-list li { position: relative; }
  .service-list .item::before {
    content: "•"; position: absolute; left: -11px; top: 0;
  }
  .service-list .sub-item { padding-left: 19px; }
  .services-left { left: 63px; top: 100px; }
  .services-left li { margin-bottom: 10.8px; }
  .services-right { left: 726px; top: 100px; width: 360px; }
  .services-right li { margin-bottom: 11px; }
  .pockets {
    position: absolute; left: 0; top: 565px; width: 1120px; height: 226px;
  }
</style>
</head>
<body>
  <main class="folder-spread">
    <div class="hex-pattern" role="img" aria-label="Hexagon network pattern in dark brown and red"></div>
    <div class="heart-mark" role="img" aria-label="Faint heart outline with heartbeat line decoration"></div>
    <div class="fold-line"></div>

    <div class="section-band"></div>
    <h1 class="section-title">Office Services Provided</h1>

    <ul class="service-list services-left">
      <li class="item">Consultation and Preventive Screening for:</li>
      <li class="sub-item">- Coronary Artery Disease</li>
      <li class="sub-item">- Peripheral Arterial/Venous Disease/Carotid Artery Disease</li>
      <li class="sub-item">- Valvular Heart Disease</li>
      <li class="sub-item">- Advanced Heart Failure</li>
      <li class="sub-item">- Lipid &amp; Blood Pressure and Blood Sugar Disorders</li>
      <li class="item">Cardiac and Vascular Ultrasound</li>
      <li class="item">Nuclear Stress Imaging</li>
      <li class="item">Arrhythmia Evaluation:</li>
      <li class="sub-item">- EKG, Holter, and Event Monitor</li>
      <li class="sub-item">- Implantable Loop Monitor</li>
    </ul>

    <ul class="service-list services-right">
      <li class="item">Lab Testing on Site</li>
      <li class="item">External Counter Pulsation Therapy for Advanced Heart Failure &amp; CAD Patients (ECP)</li>
      <li class="item">Screening for Endothelial Dysfunction &amp; Autonomic Dysfunction</li>
      <li class="item">Venous Ablation Therapy</li>
      <li class="item">Cardiac PET MPI</li>
      <li class="item">Heart Scan (Coronary Calcium Scan)</li>
      <li class="item">Pacemaker &amp; Defibrillator Interrogation</li>
    </ul>

    <svg class="pockets" viewBox="0 0 1120 226" role="img" aria-label="Two red inner pockets with soft hexagon pattern">
      <defs>
        <linearGradient id="pocketLeft" x1="0" y1="0" x2="1" y2="0">
          <stop offset="0" stop-color="var(--pocket-deep)"/>
          <stop offset="0.5" stop-color="var(--pocket-red)"/>
          <stop offset="1" stop-color="var(--pocket-red)"/>
        </linearGradient>
        <linearGradient id="pocketRight" x1="1" y1="0" x2="0" y2="0">
          <stop offset="0" stop-color="var(--pocket-deep)"/>
          <stop offset="0.5" stop-color="var(--pocket-red)"/>
          <stop offset="1" stop-color="var(--pocket-red)"/>
        </linearGradient>
      </defs>
      <polygon class="pocket-left" points="0,0 534,0 556,226 0,226" fill="url(#pocketLeft)"/>
      <polygon class="pocket-right" points="589,0 1120,0 1120,226 565,226" fill="url(#pocketRight)"/>
    </svg>
  </main>
</body>
</html>
```